Business Card Design Project

I own a dental practice and would like to use a logo that was recently designed to make business cards.
I am looking for a clean card with the following information on the card.

Halvorsen Dental Center (Using the logo)
Martin K. Halvorsen, D.D.S.
2847 Willow Bend Rd. Suite B
Colorado Springs, CO 80471
(719) 555-0186
halvorsendentalcenter@mailnest.example
www.halvorsendentalcenter.example

Also a list of items on the back:
Services include

Family Dentistry
Cosmetic
Whitening
Tooth Colored Fillings
Crowns/Bridges
Implants/Tooth Replacement
Dentures
Root Canals
Updates

Just an FYI, I added an email address and website address.

I also added my Pic.  Please give designs with and without the pic

Thanks

Target Market(s)

20-70 U.S. Female that handles the household budget.

Industry/Entity Type

Dental

Requirements
Must have
• The logo is key. The color scheme of the logo is also key. The back of the business card should have the list of Dental Services offered at the practice. The front should be clean and professional looking. No cartoons. I will also include a picture of myself. I think that the final card may or may not include this picture, so the card designs should come with and without the picture. USE THE BLUE LOGO ONLY!!!
Should not have
• NO teeth should be on the card.

```html
<!DOCTYPE html>
<html lang="en">
<head>
<meta charset="utf-8">
<title>Halvorsen Dental Center – Business Card</title>
<link rel="stylesheet" href="https://fonts.googleapis.com/css2?family=Open+Sans:wght@400;600;700&display=swap">
<style>
  :root {
    --teal: #3f6f82;
    --teal-dark: #2c5566;
    --teal-light: #6f98a8;
    --brown: #4e4541;
    --ink: #4a4a4a;
    --white: #ffffff;
    --page: #e9e6e1;
    --photo-a: #3a3a40;
    --photo-b: #7d6f86;
  }
  * { box-sizing: border-box; margin: 0; padding: 0; }
  html, body { width: 1200px; height: 1024px; overflow: hidden; }
  body {
    background: var(--page);
    font-family: "Open Sans", Arial, sans-serif;
    color: var(--ink);
    position: relative;
  }
  .card {
    position: absolute;
    left: 190px;
    width: 820px;
    height: 469px;
    border-radius: 4px;
    overflow: hidden;
    box-shadow: 0 6px 18px rgba(0,0,0,0.18);
  }
  .card-front { top: 26px; background: var(--white); }
  .card-back {
    top: 529px;
    background: linear-gradient(135deg, var(--teal-light) 0%, var(--teal) 45%, var(--teal-dark) 100%);
    color: var(--white);
  }
  .card-art { position: absolute; inset: 0; }
  .photo {
    position: absolute;
    left: 420px; top: 0;
    width: 360px; height: 300px;
    background: linear-gradient(160deg, var(--photo-b), var(--photo-a));
  }
  .brand {
    position: absolute;
    display: flex;
    align-items: center;
    gap: 12px;
  }
  .brand-mark {
    width: 30px; height: 30px;
    border-radius: 50%;
    background: var(--teal);
    flex: none;
  }
  .brand-name {
    font-size: 26px;
    font-weight: 600;
    color: var(--teal);
    letter-spacing: 0.3px;
    line-height: 1.15;
    width: 200px;
  }
  .card-front .brand { left: 44px; top: 120px; }
  .contact {
    position: absolute;
    left: 44px; top: 222px;
    font-size: 15px;
    line-height: 1.55;
  }
  .contact-name {
    font-size: 19px;
    font-weight: 700;
    color: var(--teal);
    margin-bottom: 4px;
    letter-spacing: 0.5px;
  }
  .contact-name .degree { color: var(--ink); font-size: 16px; }
  .contact-row { display: flex; align-items: center; gap: 8px; }
  .contact-row svg { width: 15px; height: 15px; flex: none; }
  .website-front {
    position: absolute;
    right: 30px; bottom: 34px;
    font-size: 15px;
    color: var(--white);
    letter-spacing: 0.3px;
  }
  .appointment {
    position: absolute;
    left: 50px; top: 42px;
    width: 400px;
    font-size: 17px;
  }
  .appointment h2 { font-size: 18px; font-weight: 400; margin-bottom: 8px; }
  .appt-line {
    display: flex;
    align-items: flex-end;
    gap: 8px;
    height: 34px;
  }
  .appt-line .rule { flex: 1; border-bottom: 1px solid rgba(255,255,255,0.8); height: 1px; margin-bottom: 6px; }
  .card-back .brand { right: 50px; top: 80px; }
  .card-back .brand-mark { background: var(--white); }
  .card-back .brand-name { color: var(--white); }
  .services {
    position: absolute;
    left: 50px; top: 270px;
    font-size: 17px;
    line-height: 1.7;
  }
  .services span + span::before { content: "\25CF"; font-size: 10px; margin: 0 9px; vertical-align: 2px; }
  .website-back { position: absolute; left: 50px; top: 360px; font-size: 14px; }
</style>
</head>
<body>

<section class="card card-front">
  <div class="photo" role="img" aria-label="Portrait photo of the dentist"></div>
  <svg class="card-art" viewBox="0 0 820 469" aria-hidden="true">
    <path d="M0,430 C260,430 520,360 820,96 L820,469 L0,469 Z" fill="var(--brown)"/>
    <path d="M0,446 C270,446 530,376 820,118 L820,469 L0,469 Z" fill="var(--white)"/>
    <path d="M0,454 C275,454 535,386 820,128 L820,469 L0,469 Z" fill="var(--teal)"/>
  </svg>
  <div class="brand">
    <span class="brand-mark"></span>
    <span class="brand-name">Halvorsen Dental Center</span>
  </div>
  <div class="contact">
    <div class="contact-name">MARTIN K. HALVORSEN | <span class="degree">D.D.S.</span></div>
    <div>2847 Willow Bend Rd. Suite B</div>
    <div>Colorado Springs, CO 80471</div>
    <div class="contact-row">
      <svg viewBox="0 0 24 24"><path fill="var(--teal)" d="M6.6 10.8a15 15 0 0 0 6.6 6.6l2.2-2.2a1 1 0 0 1 1-.25 11.4 11.4 0 0 0 3.6.57 1 1 0 0 1 1 1V20a1 1 0 0 1-1 1A17 17 0 0 1 3 4a1 1 0 0 1 1-1h3.5a1 1 0 0 1 1 1c0 1.25.2 2.45.57 3.57a1 1 0 0 1-.25 1z"/></svg>
      <span>(719) 555-0186</span>
    </div>
    <div class="contact-row">
      <svg viewBox="0 0 24 24"><rect x="2" y="5" width="20" height="14" rx="1" fill="none" stroke="var(--teal)" stroke-width="2"/><path d="M2 6l10 7 10-7" fill="none" stroke="var(--teal)" stroke-width="2"/></svg>
      <span>halvorsendentalcenter@mailnest.example</span>
    </div>
  </div>
  <div class="website-front">www.halvorsendentalcenter.example</div>
</section>

<section class="card card-back">
  <div class="appointment">
    <h2>Appointment</h2>
    <div class="appt-line"><span>For:</span><span class="rule"></span></div>
    <div class="appt-line"><span>Day:</span><span class="rule"></span></div>
    <div class="appt-line"><span>Date:</span><span class="rule"></span></div>
    <div class="appt-line"><span>Time:</span><span class="rule"></span></div>
  </div>
  <div class="brand">
    <span class="brand-mark"></span>
    <span class="brand-name">Halvorsen Dental Center</span>
  </div>
  <div class="services">
    <div><span>Family Dentistry</span><span>Cosmetic</span><span>Whitening</span><span>Tooth Colored Fillings</span></div>
    <div><span>Crowns/Bridges</span><span>Implants/Tooth Replacement</span><span>Dentures</span><span>Root Canals</span></div>
  </div>
  <div class="website-back">www.halvorsendentalcenter.example</div>
</section>

</body>
</html>
```